Project Title:
Dental Implant Overdenture Flyer (Retirement Village Target)
Objective:
Create a clean, trustworthy, and reassuring flyer aimed at older adults (60–85 years old) who struggle with loose dentures. The goal is to educate them about implant-retained “clip-on” dentures and encourage them to book a consultation.
Tone & Feel:
Warm, caring, non-intimidating
Premium but not “salesy”
Medical but easy to understand
Focus on improving quality of life (confidence, eating, comfort)
Target Audience:
Retirees / pensioners
Existing denture wearers
People frustrated with loose or uncomfortable dentures
Key Message:
“You don’t have to live with loose dentures anymore.”
Design Style:
Clean, minimal, modern
Soft colours (blues, greens, warm neutrals)
Easy-to-read large font
High contrast for older eyes
Avoid clutter
Imagery Suggestions:
Smiling older adults (natural, not stocky/overly staged)
Before/after lifestyle (eating, laughing, socialising)
Simple diagram showing denture clipping onto implants
Avoid graphic surgical images
Layout Suggestions:
A5 or DL flyer
Clear sections with headings
Icons for benefits
Strong call-to-action at bottom
HEADLINE (big and bold)
Tired of Loose Dentures?
Discover Secure “Clip-On” Teeth
🔹 PROBLEM SECTION
Do your dentures:
Slip or move when eating?
Make it hard to chew certain foods?
Feel uncomfortable or loose?
Affect your confidence when speaking or smiling?
You’re not alone — and there is a better solution.
🔹 SOLUTION SECTION
Implant-Retained “Clip-On” Dentures
We can secure your denture using just 2 dental implants, allowing your teeth to:
✔ Stay firmly in place
✔ Improve your ability to eat
✔ Feel more comfortable
✔ Boost your confidence
🔹 SIMPLE EXPLANATION (very important)
Small titanium implants are gently placed in the jaw.
Your denture then clips securely onto them, stopping movement.
🔹 PRICE SECTION (highlight this clearly)
$12,000
Includes:
2 dental implants
A brand new custom overdenture
Does not include sedation or extractions (if needed)
🔹 SEDATION
Sedation is available for comfort.
If you hold a pensioner card, you may receive a significant Vantacor rebate, often resulting in minimal out-of-pocket costs for sedation.
🔹 TRUST / REASSURANCE
Experienced implant clinician
Gentle, patient-focused care
Modern technology and techniques
🔹 CALL TO ACTION (VERY IMPORTANT)
Book a Free Consultation
📞 Call: 08 9351 4276
🌐 Visit: www.bravonclinic.com.au
📍 Located near Tallowmere shopping centre
🔹 OPTIONAL TAGLINE
Eat Better. Feel Better. Smile with Confidence Again.
Please include some photos to illustrate what a clip on denture looks like with two implants.

```html
<!DOCTYPE html>
<html lang="en">
<head>
<meta charset="utf-8">
<title>Clip-On Dentures Flyer</title>
<link href="https://fonts.googleapis.com/css2?family=Montserrat:wght@400;500;600;700;800&display=swap" rel="stylesheet">
<style>
:root{
  --backdrop:#cccccc;
  --paper:#ffffff;
  --ink:#111111;
  --teal:#0097b2;
  --teal-soft:#b3f5f1;
  --aqua:#21d5cc;
  --aqua-dark:#15c2c4;
  --white:#ffffff;
}
*{margin:0;padding:0;box-sizing:border-box}
html,body{width:1200px;height:1200px;overflow:hidden}
body{background:var(--backdrop);font-family:'Montserrat',sans-serif;color:var(--ink);position:relative}
.flyer{position:absolute;left:242px;top:91px;width:717px;height:1017px;background:var(--paper);overflow:hidden}
.flyer > *{position:absolute}
.headline{left:29px;top:30px;font-size:50px;font-weight:800;line-height:57px;letter-spacing:-0.5px}
.subhead{left:29px;top:145px;font-size:26px;font-weight:500;line-height:32px}
.problem-band{left:0;top:215px;width:717px;height:208px;background:var(--teal)}
.couple-photo{left:398px;top:14px;width:319px;height:336px;border-radius:160px 160px 0 60px;
  background:radial-gradient(ellipse at 55% 40%,#f1ddd0 0%,#d9dde2 35%,#7ea6cf 70%,rgba(0,151,178,0) 100%)}
.problem-title{left:29px;top:230px;font-size:22px;font-weight:700;color:var(--white);line-height:26px}
.ticks{list-style:none}
.ticks li{display:flex;align-items:center;gap:4px;white-space:nowrap}
.ticks svg{width:16px;height:16px;flex:none}
.problem-list{left:29px;top:262px;color:var(--white);font-size:17px;font-weight:500}
.problem-list li{height:25.5px}
.reassure{left:30px;top:386px;font-size:17px;font-weight:700;color:var(--white)}
.solution-title{left:27px;top:438px;font-size:22px;font-weight:700}
.solution-intro{left:29px;top:474px;font-size:17px;font-weight:600;line-height:21px}
.benefit-list{left:29px;top:531px;font-size:17.5px;font-weight:500}
.benefit-list li{height:25.5px}
.denture-photo{left:398px;top:480px;width:273px;height:168px;border-radius:30% 30% 50% 50%/25% 25% 75% 75%;
  background:radial-gradient(ellipse at 50% 40%,#ffffff 0%,#f2d8d3 40%,#dd9d97 75%,rgba(255,255,255,0) 100%)}
.price-box{left:32px;top:665px;width:313px;height:167px;background:var(--teal);border-radius:9px;color:var(--white);padding:6px 10px}
.price{font-size:40px;font-weight:800;letter-spacing:-1px;line-height:42px}
.includes{font-size:15px;font-weight:600;line-height:20px}
.price-list{font-size:15px;font-weight:500;margin-top:3px}
.price-list li{align-items:flex-start;line-height:20px}
.price-list li:nth-child(2){margin-top:6px}
.price-list li:nth-child(3){margin-top:3px}
.price-list svg{margin-top:3px}
.explain{left:381px;top:670px;font-size:13px;font-weight:500;line-height:17px;white-space:nowrap}
.trust-box{left:374px;top:735px;width:313px;height:97px;background:var(--teal-soft);border-radius:10px;padding:10px 13px;font-size:15px;font-weight:500;list-style:none}
.trust-box li{height:25px;display:flex;align-items:center;gap:5px;white-space:nowrap}
.trust-box svg{width:15px;height:16px;flex:none}
.brand{left:32px;top:890px;display:flex;align-items:center;gap:10px;font-size:20px;font-weight:700;color:var(--teal)}
.brand-dot{width:16px;height:16px;border-radius:50%;background:var(--aqua)}
.cta{left:253px;top:859px;width:434px;height:89px;background:var(--aqua);border-radius:10px;overflow:hidden}
.cta-tab{position:absolute;left:0;top:0;width:292px;height:27px;background:var(--aqua-dark);clip-path:polygon(0 0,100% 0,93% 100%,0 100%)}
.cta-title{position:absolute;left:10px;top:2px;font-size:20px;font-weight:700;color:var(--white)}
.cta-row{position:absolute;display:flex;align-items:center;gap:4px;font-size:19px;font-weight:700;color:var(--ink);white-space:nowrap}
.cta-row svg{width:14px;height:16px;flex:none}
.cta-phone{left:14px;top:36px}
.cta-web{left:188px;top:39px;font-size:15px}
.cta-place{left:14px;top:63px;font-size:17px}
.tagline{left:0;top:965px;width:717px;text-align:center;font-size:17px;font-weight:600}
.base-bar{left:0;top:1000px;width:717px;height:17px;background:var(--aqua)}
</style>
</head>
<body>
<main class="flyer">
  <h1 class="headline">Tired of Loose<br>Dentures?</h1>
  <p class="subhead">Discover Secure<br>“Clip-On” Teeth</p>

  <div class="problem-band"></div>
  <div class="couple-photo" role="img" aria-label="Photo of a smiling older couple embracing"></div>
  <h2 class="problem-title">Do your dentures</h2>
  <ul class="ticks problem-list">
    <li><svg viewBox="0 0 16 16"><path d="M2 8.5l4 4 8-9" fill="none" stroke="#fff" stroke-width="2"/></svg>Slip or move when eating?</li>
    <li><svg viewBox="0 0 16 16"><path d="M2 8.5l4 4 8-9" fill="none" stroke="#fff" stroke-width="2"/></svg>Make it hard to chew certain foods?</li>
    <li><svg viewBox="0 0 16 16"><path d="M2 8.5l4 4 8-9" fill="none" stroke="#fff" stroke-width="2"/></svg>Feel uncomfortable or loose?</li>
    <li><svg viewBox="0 0 16 16"><path d="M2 8.5l4 4 8-9" fill="none" stroke="#fff" stroke-width="2"/></svg>Affect your confidence when speaking or smiling?</li>
  </ul>
  <p class="reassure">You’re not alone — and there is a better solution.</p>

  <h2 class="solution-title">Implant-Retained “Clip-On” Dentures</h2>
  <p class="solution-intro">We can secure your denture using just<br>2 dental implants, allowing your teeth to:</p>
  <ul class="ticks benefit-list">
    <li><svg viewBox="0 0 16 16"><path d="M2 8.5l4 4 8-9" fill="none" stroke="#111" stroke-width="2"/></svg>Stay firmly in place</li>
    <li><svg viewBox="0 0 16 16"><path d="M2 8.5l4 4 8-9" fill="none" stroke="#111" stroke-width="2"/></svg>Improve your ability to eat</li>
    <li><svg viewBox="0 0 16 16"><path d="M2 8.5l4 4 8-9" fill="none" stroke="#111" stroke-width="2"/></svg>Feel more comfortable</li>
    <li><svg viewBox="0 0 16 16"><path d="M2 8.5l4 4 8-9" fill="none" stroke="#111" stroke-width="2"/></svg>Boost your confidence</li>
  </ul>
  <div class="denture-photo" role="img" aria-label="Illustration of a lower overdenture clipping onto two titanium implants"></div>

  <section class="price-box">
    <p class="price">$12,000</p>
    <p class="includes">Includes:</p>
    <ul class="ticks price-list">
      <li><svg viewBox="0 0 16 16"><path d="M2 8.5l4 4 8-9" fill="none" stroke="#fff" stroke-width="2"/></svg>2 dental implants</li>
      <li><svg viewBox="0 0 16 16"><path d="M2 8.5l4 4 8-9" fill="none" stroke="#fff" stroke-width="2"/></svg>A brand new custom overdenture</li>
      <li><svg viewBox="0 0 16 16"><path d="M2 8.5l4 4 8-9" fill="none" stroke="#fff" stroke-width="2"/></svg><span>Does not include sedation or<br>extractions (if needed)</span></li>
    </ul>
  </section>

  <p class="explain">Small titanium implants are gently placed<br>in the jaw. Your denture then clips securely<br>onto them, stopping movement.</p>

  <ul class="trust-box">
    <li><svg viewBox="0 0 15 16"><path d="M7.5 0L15 3v5c0 4-3.5 7-7.5 8C3.5 15 0 12 0 8V3z" fill="#0097b2"/><path d="M4 8l2.5 2.5L11 5.5" fill="none" stroke="#b3f5f1" stroke-width="1.6"/></svg>Sedation is available for comfort.</li>
    <li><svg viewBox="0 0 15 16"><path d="M7.5 0L15 3v5c0 4-3.5 7-7.5 8C3.5 15 0 12 0 8V3z" fill="#0097b2"/><path d="M4 8l2.5 2.5L11 5.5" fill="none" stroke="#b3f5f1" stroke-width="1.6"/></svg>Experienced implant clinician</li>
    <li><svg viewBox="0 0 15 16"><path d="M7.5 0L15 3v5c0 4-3.5 7-7.5 8C3.5 15 0 12 0 8V3z" fill="#0097b2"/><path d="M4 8l2.5 2.5L11 5.5" fill="none" stroke="#b3f5f1" stroke-width="1.6"/></svg>Gentle, patient-focused care</li>
  </ul>

  <div class="brand"><span class="brand-dot"></span>Bravon Clinic</div>

  <section class="cta">
    <div class="cta-tab"></div>
    <h2 class="cta-title">Book a Free Consultation</h2>
    <p class="cta-row cta-phone"><svg viewBox="0 0 14 16"><path d="M3 1l3 3-1.5 2c1 2 2.5 3.5 4.5 4.5L11 9l3 3-2 2.5C6 14 1 9 .5 3z" fill="#111"/></svg>08 9351 4276</p>
    <p class="cta-row cta-web"><svg viewBox="0 0 16 16"><circle cx="8" cy="8" r="7" fill="none" stroke="#111" stroke-width="1.3"/><ellipse cx="8" cy="8" rx="3" ry="7" fill="none" stroke="#111" stroke-width="1.1"/><path d="M1 8h14M2.5 4.5h11M2.5 11.5h11" stroke="#111" stroke-width="1.1"/></svg>www.bravonclinic.com.au</p>
    <p class="cta-row cta-place"><svg viewBox="0 0 14 16"><path d="M7 1a5 5 0 0 1 5 5c0 4-5 8-5 8S2 10 2 6a5 5 0 0 1 5-5z" fill="none" stroke="#111" stroke-width="1.6"/><circle cx="7" cy="6" r="1.8" fill="#111"/></svg>Near Tallowmere Shopping Centre</p>
  </section>

  <p class="tagline">Eat Better. Feel Better. Smile with Confidence Again.</p>
  <div class="base-bar"></div>
</main>
</body>
</html>
```